Business card design needed

Business Card design required for new small plumbing business.
Would like a logo/text look that is simple and unique and does not have to be representative of a plumbing company (ie. having a cartoon plumber or toilet etc) as the companyname is self explanatory.
Would like the main colour to be green (lime green).

Industry/Entity Type

Plumber

Contact Information for Business Card

BRISCOMB PLUMBING
ABN 61 947 205 318 004

Harold Tenfield
Licensed Plumber 71635
Phone: 0477 261 408

27 Worrell Drive,
Langwarrin. 3910 Victoria

Email: briscombplumbing@mailora.net

Logo Text

Briscomb Plumbing

Logo styles of interest
Character Logo
Wordmark Logo
Lettermark Logo

```html
<!DOCTYPE html>
<html lang="en">
<head>
<meta charset="utf-8">
<title>Briscomb Plumbing – Business Card</title>
<link rel="stylesheet" href="https://fonts.googleapis.com/css2?family=Roboto:wght@400;700;900&display=swap">
<style>
  :root {
    --page-bg: #ecece6;
    --lime: #b4d80c;
    --lime-light: #d3ee4a;
    --lime-pale: #e6f79a;
    --lime-deep: #9cc20a;
    --card-white: #ffffff;
    --text-green: #557d0c;
    --text-olive: #5d7a12;
    --accent-blue: #35a7c8;
    --text-white: #ffffff;
  }
  * { box-sizing: border-box; margin: 0; padding: 0; }
  html, body {
    width: 1200px; height: 900px; overflow: hidden;
    background: var(--page-bg);
    font-family: "Roboto", Arial, sans-serif;
  }
  .card {
    position: absolute; left: 300px;
    width: 600px; height: 343px;
    overflow: hidden;
    box-shadow: 0 8px 22px rgba(0,0,0,0.18);
  }
  .card--front { top: 80px; }
  .card--back { top: 470px; }
  .card__art { position: absolute; inset: 0; width: 100%; height: 100%; }

  .brand {
    position: absolute; display: flex; align-items: center;
    color: var(--text-green); font-weight: 900; letter-spacing: 0.5px;
  }
  .brand__square { background: var(--accent-blue); flex: none; }
  .card--front .brand { left: 250px; top: 70px; font-size: 26px; gap: 12px; }
  .card--front .brand__square { width: 34px; height: 34px; }
  .card--back .brand { right: 28px; top: 38px; font-size: 19px; gap: 9px; }
  .card--back .brand__square { width: 24px; height: 24px; }

  .holder { position: absolute; right: 34px; top: 104px; text-align: center; color: var(--text-olive); }
  .holder__name { font-size: 32px; font-weight: 700; }
  .holder__role { font-size: 17px; font-weight: 400; margin-top: 2px; }

  .services {
    position: absolute; left: 38px; top: 148px; list-style: none;
    color: var(--text-white); font-weight: 700; font-size: 16.5px; line-height: 20px;
    text-transform: uppercase;
  }
  .details {
    position: absolute; left: 28px; top: 240px;
    color: var(--text-green); font-weight: 700; font-size: 17px; line-height: 23px;
  }
  .phone {
    position: absolute; right: 30px; bottom: 26px;
    color: var(--text-green); font-weight: 700; font-size: 24px;
  }
</style>
</head>
<body>

<section class="card card--front" aria-label="Card front">
  <svg class="card__art" viewBox="0 0 600 343" preserveAspectRatio="none" aria-hidden="true">
    <rect width="600" height="343" fill="var(--lime)"/>
    <ellipse cx="440" cy="90" rx="470" ry="250" fill="var(--lime-deep)"/>
    <ellipse cx="450" cy="80" rx="430" ry="225" fill="var(--lime-light)"/>
    <ellipse cx="460" cy="70" rx="400" ry="205" fill="var(--lime-pale)"/>
    <ellipse cx="470" cy="60" rx="380" ry="190" fill="var(--card-white)"/>
  </svg>
  <div class="brand">
    <span class="brand__square"></span>
    <span class="brand__name">BRISCOMB PLUMBING</span>
  </div>
</section>

<section class="card card--back" aria-label="Card back">
  <svg class="card__art" viewBox="0 0 600 343" preserveAspectRatio="none" aria-hidden="true">
    <rect width="600" height="343" fill="var(--lime)"/>
    <ellipse cx="440" cy="95" rx="400" ry="210" fill="var(--lime-deep)"/>
    <ellipse cx="450" cy="90" rx="370" ry="190" fill="var(--lime-light)"/>
    <ellipse cx="460" cy="85" rx="345" ry="175" fill="var(--lime-pale)"/>
    <ellipse cx="470" cy="80" rx="325" ry="165" fill="var(--card-white)"/>
  </svg>

  <div class="brand">
    <span class="brand__square"></span>
    <span class="brand__name">BRISCOMB PLUMBING</span>
  </div>

  <div class="holder">
    <p class="holder__name">Harold Tenfield</p>
    <p class="holder__role">Licensed Plumber</p>
  </div>

  <ul class="services">
    <li>Hot Water</li>
    <li>Water Renewal</li>
    <li>Blocked Drains</li>
    <li>Maintenance &amp; Repairs</li>
  </ul>

  <div class="details">
    <p class="details__email">briscombplumbing@mailora.net</p>
    <p class="details__abn">ABN 61 947 205 318 004</p>
  </div>

  <p class="phone">Ph: 0477 261 408</p>
</section>

</body>
</html>
```